Flyer für Anbieter für Rennstrecken-trainings
Zielgruppe
wir sind ein professioneller Anbieter für Rennstrecken-trainings ( Motorrad). unsere Zielgruppe sind Motorsport begeisterte jeden alters.
Aufgabenstellung
Ein cleanes modernes design , es gibt exacte vorstellungen

```html
<!DOCTYPE html>
<html lang="de">
<head>
<meta charset="utf-8">
<title>Rennstrecken-Coaching Flyer</title>
<link rel="stylesheet" href="https://fonts.googleapis.com/css2?family=Montserrat:ital,wght@1,700;1,800;1,900&family=Saira:ital,wght@1,800;1,900&display=swap">
<style>
  :root {
    --dark: #16231a;
    --darker: #101a12;
    --green: #8cc63f;
    --green-light: #a3cf45;
    --green-deep: #3f8a2c;
    --yellow: #ffcc0a;
    --white: #ffffff;
    --ink: #142013;
  }
  * { margin: 0; padding: 0; box-sizing: border-box; }
  html, body { width: 907px; height: 1200px; overflow: hidden; background: #e9e9ea; }
  .flyer {
    position: relative; width: 907px; height: 1200px; overflow: hidden;
    background: var(--dark);
    font-family: "Montserrat", sans-serif; font-style: italic; color: var(--white);
  }
  .abs { position: absolute; }
  .top-glow { left: 0; top: 0; width: 907px; height: 242px; }
  .track-photo {
    left: 0; top: 241px; width: 907px; height: 959px;
    background:
      linear-gradient(160deg, #c9d3d6 0%, #8d9296 18%, #6f7377 40%, #8a4a4a 62%, #58684a 78%, #47573a 100%);
  }
  .track-shade {
    left: 0; top: 241px; width: 907px; height: 959px;
    background: linear-gradient(100deg, rgba(20,33,24,.97) 0%, rgba(20,33,24,.93) 38%, rgba(20,33,24,.35) 62%, rgba(20,33,24,0) 78%),
                linear-gradient(0deg, rgba(20,33,24,.55) 0%, rgba(20,33,24,0) 35%);
  }
  .band { position: absolute; }
  .band svg { position: absolute; left: 0; top: 0; }
  .band-text {
    position: absolute; font-weight: 900; color: var(--ink); white-space: nowrap;
  }
  .title {
    font-family: "Saira", sans-serif; font-weight: 900; font-size: 47px; letter-spacing: -1px;
    color: var(--ink); text-shadow: -2px -2px 0 var(--yellow);
  }
  .cta {
    font-family: "Saira", sans-serif; font-weight: 900; font-size: 42px; letter-spacing: -1px;
    color: var(--ink); text-shadow: -2px -2px 0 var(--yellow);
  }
  .rule { left: 52px; top: 130px; width: 800px; height: 3px;
    background: linear-gradient(90deg, rgba(140,198,63,0), var(--green) 20%, var(--green) 80%, rgba(140,198,63,0)); }
  .price-line { left: 54px; top: 146px; white-space: nowrap; font-family: "Saira", sans-serif; font-weight: 900; }
  .price-line .small { font-size: 30px; color: var(--yellow); }
  .price-line .big { font-size: 48px; color: var(--yellow); }
  .price-line .rest { font-size: 31px; color: var(--white); }
  .feature { left: 22px; display: flex; align-items: center; gap: 18px; }
  .feature svg { width: 38px; height: 30px; }
  .feature span { font-size: 24px; font-weight: 800; letter-spacing: 4.5px; }
  .divider { left: 22px; height: 1px; background: rgba(255,255,255,.35); }
  .prog { left: 30px; display: flex; gap: 10px; align-items: flex-start; }
  .prog svg { width: 26px; height: 28px; margin-top: 4px; }
  .prog .main { font-size: 22px; font-weight: 800; letter-spacing: 3px; line-height: 22px; }
  .prog .sub { font-size: 13.5px; font-weight: 800; letter-spacing: 1.8px; color: var(--yellow); line-height: 16px; }
  .prog .sub.tiny { font-size: 11px; letter-spacing: 1.6px; }
  .gear-photo { left: 34px; top: 746px; width: 180px; height: 236px;
    background: radial-gradient(ellipse at 45% 45%, #3d4a3a 0%, #222a22 55%, rgba(22,35,26,0) 80%); }
  .gear-list { left: 148px; top: 762px; list-style: none; }
  .gear-list li { font-size: 22px; font-weight: 800; letter-spacing: 3px; line-height: 35.5px; }
  .bundle { left: 492px; top: 806px; width: 300px; height: 136px; }
  .bundle-price { position: absolute; left: 44px; top: -6px; width: 230px; text-align: center;
    font-family: "Montserrat", sans-serif; font-weight: 900; font-size: 76px; letter-spacing: -5px; color: var(--ink); }
  .bundle-label { position: absolute; left: 24px; top: 98px; width: 230px; text-align: center;
    font-style: normal; font-weight: 800; font-size: 19px; color: var(--ink); }
  .hygiene { left: 34px; top: 995px; display: flex; gap: 12px; }
  .hygiene svg { width: 56px; height: 56px; }
  .hygiene p { margin-top: 12px; font-size: 15px; font-weight: 800; letter-spacing: 1px; line-height: 22px; }
  .audience { left: 34px; top: 1146px; font-size: 19px; font-weight: 800; letter-spacing: 3.5px; }
</style>
</head>
<body>
<main class="flyer">
  <svg class="abs top-glow" viewBox="0 0 907 242" aria-hidden="true">
    <defs>
      <linearGradient id="glow" x1="0" y1="0" x2="1" y2="1">
        <stop offset="0" stop-color="#5aa33a"/>
        <stop offset="1" stop-color="#a3cf45"/>
      </linearGradient>
    </defs>
    <rect width="907" height="242" fill="var(--dark)"/>
    <polygon points="650,0 907,0 907,242 528,242" fill="url(#glow)"/>
  </svg>

  <div class="abs track-photo" role="img" aria-label="Foto: Rennfahrer in grün-schwarzer Lederkombi auf grünem Supersportmotorrad in Schräglage auf der Rennstrecke, rot-weiße Curbs und Rasen"></div>
  <div class="abs track-shade" aria-hidden="true"></div>

  <!-- headline -->
  <div class="band" style="left:34px;top:41px;width:860px;height:66px;">
    <svg width="860" height="66" aria-hidden="true">
      <polygon points="22,0 860,0 836,66 0,66" fill="var(--ink)"/>
      <polygon points="20,0 848,0 826,58 0,58" fill="var(--green)"/>
    </svg>
    <h1 class="band-text title" style="left:32px;top:-2px;">RENNSTRECKEN-COACHING</h1>
  </div>
  <div class="abs rule"></div>

  <p class="abs price-line"><span class="small">NUR </span><span class="big">349€</span><span class="rest"> PRO FAHRER</span></p>

  <!-- included -->
  <div class="band" style="left:0;top:219px;width:502px;height:48px;">
    <svg width="502" height="48" aria-hidden="true">
      <polygon points="0,0 502,0 484,48 0,48" fill="var(--green)"/>
    </svg>
    <h2 class="band-text" style="left:22px;top:4px;font-size:32px;">IM PREIS ENTHALTEN:</h2>
  </div>

  <div class="abs feature" style="top:292px;">
    <svg viewBox="0 0 38 30" aria-hidden="true"><g fill="none" stroke="var(--yellow)" stroke-width="3"><circle cx="8" cy="21" r="6"/><circle cx="30" cy="21" r="6"/></g><path d="M8 21 L16 12 H24 L30 21 M20 12 L24 6 H28" fill="none" stroke="var(--yellow)" stroke-width="3"/></svg>
    <span>KESTREL KR-400</span>
  </div>
  <div class="abs divider" style="top:326px;width:480px;"></div>
  <div class="abs feature" style="top:339px;">
    <svg viewBox="0 0 38 30" aria-hidden="true"><rect x="6" y="2" width="16" height="26" rx="2" fill="var(--yellow)"/><rect x="9" y="6" width="10" height="7" fill="var(--dark)"/><path d="M22 8 L28 12 V24 a2 2 0 0 0 4 0 V12" fill="none" stroke="var(--yellow)" stroke-width="2.5"/></svg>
    <span>SPRIT</span>
  </div>
  <div class="abs divider" style="top:376px;width:470px;"></div>
  <div class="abs feature" style="top:386px;">
    <svg viewBox="0 0 38 30" aria-hidden="true"><circle cx="19" cy="15" r="13" fill="var(--yellow)"/><circle cx="19" cy="15" r="8" fill="none" stroke="var(--dark)" stroke-width="2.5"/><circle cx="19" cy="15" r="2.5" fill="var(--dark)"/></svg>
    <span>REIFENWÄRMER</span>
  </div>
  <div class="abs divider" style="top:431px;width:455px;"></div>
  <div class="abs feature" style="top:444px;">
    <svg viewBox="0 0 38 30" aria-hidden="true"><path d="M4 20 C4 8 14 2 24 3 C33 4 36 12 35 18 L20 18 L18 26 L8 26 C5 25 4 23 4 20 Z" fill="var(--yellow)"/><path d="M20 12 H34" stroke="var(--dark)" stroke-width="3"/></svg>
    <span>PROFI-TRAINER</span>
  </div>

  <!-- program -->
  <div class="band" style="left:0;top:504px;width:528px;height:56px;">
    <svg width="528" height="56" aria-hidden="true">
      <polygon points="0,0 528,0 506,56 0,56" fill="var(--ink)"/>
      <polygon points="0,0 520,0 500,50 0,50" fill="var(--green)"/>
    </svg>
    <h2 class="band-text" style="left:20px;top:5px;font-size:33px;">TRAININGS PROGRAMM</h2>
  </div>
  <div class="abs prog" style="top:572px;">
    <svg viewBox="0 0 26 28" aria-hidden="true"><circle cx="13" cy="16" r="10" fill="none" stroke="var(--yellow)" stroke-width="3"/><rect x="10" y="1" width="6" height="3" fill="var(--yellow)"/><path d="M13 16 L13 10" stroke="var(--yellow)" stroke-width="2.5"/></svg>
    <div><div class="main">3,5 STUNDEN</div><div class="sub">INTENSIVTRAINING</div></div>
  </div>
  <div class="abs prog" style="top:620px;">
    <svg viewBox="0 0 26 28" aria-hidden="true"><path d="M3 26 V4" stroke="var(--yellow)" stroke-width="2.5"/><rect x="4" y="4" width="20" height="14" fill="none" stroke="var(--yellow)" stroke-width="2"/><g fill="var(--yellow)"><rect x="4" y="4" width="5" height="5"/><rect x="14" y="4" width="5" height="5"/><rect x="9" y="9" width="5" height="4"/><rect x="19" y="9" width="5" height="4"/><rect x="4" y="13" width="5" height="5"/><rect x="14" y="13" width="5" height="5"/></g></svg>
    <div><div class="main">MINDESTENS</div><div class="sub tiny">6 TURNS À 20 MINUTEN</div></div>
  </div>

  <!-- gear -->
  <div class="band" style="left:0;top:674px;width:730px;height:60px;">
    <svg width="730" height="60" aria-hidden="true">
      <polygon points="0,0 730,0 708,60 0,60" fill="var(--ink)"/>
      <polygon points="0,0 722,0 702,54 0,54" fill="var(--green)"/>
    </svg>
    <h2 class="band-text" style="left:16px;top:6px;font-size:33px;">OPTIONALE SCHUTZAUSRÜSTUNG:</h2>
  </div>
  <div class="abs gear-photo" role="img" aria-label="Produktfoto: Lederkombi, Stiefel, Helm und Handschuhe in Schwarz, Weiß und Grün"></div>
  <ul class="abs gear-list">
    <li>LEDERKOMBI 59 €</li>
    <li>HELM 29 €</li>
    <li>STIEFEL 29 €</li>
    <li>HANDSCHUHE 19 €</li>
  </ul>
  <div class="abs bundle">
    <svg width="300" height="136" aria-hidden="true">
      <path d="M30 0 H300 L278 118 Q274 136 256 136 H0 L26 8 Q28 0 30 0 Z" fill="var(--yellow)"/>
    </svg>
    <div class="bundle-price">99€</div>
    <div class="bundle-label">KOMPLETTPAKET</div>
  </div>

  <div class="abs hygiene">
    <svg viewBox="0 0 56 56" aria-hidden="true" fill="var(--yellow)"><path d="M12 2 L14 10 L22 12 L14 14 L12 22 L10 14 L2 12 L10 10 Z"/><path d="M34 14 L37 30 L53 33 L37 36 L34 52 L31 36 L15 33 L31 30 Z"/></svg>
    <p>SÄMTLICHE LEIH-AUSRÜSTUNG WIRD STETS MIT<br>OZONDESINFIZIERT UND GEREINIGT.</p>
  </div>

  <!-- call to action -->
  <div class="band" style="left:0;top:1074px;width:856px;height:56px;">
    <svg width="856" height="56" aria-hidden="true">
      <polygon points="0,0 856,0 834,56 0,56" fill="var(--ink)"/>
      <polygon points="0,0 848,0 828,50 0,50" fill="var(--green)"/>
    </svg>
    <h2 class="band-text cta" style="left:38px;top:-4px;">JETZT BUCHEN &amp; DURCHSTARTEN!</h2>
  </div>
  <p class="abs audience">FÜR EINSTEIGER &amp; FORTGESCHRITTENE</p>
</main>
</body>
</html>
```